New Look for Existing Website
Keep it simple, clean, crisp & clear
Creative Brief
Automotive
www.bitlocate.ie
We are an advertising website where people search for and view lists of results and associated information for second hand car parts suppliers.
we like Zorvane for its simplicity. We like clean and simple websites, easy to navigate and not cluttered with lots of links/advertisements or too much text.
www.zorvane.ie
http://www.klimbrook.ie/klimbrook/publish/vehicleLookup.jsp
please view the existing website at www.bitlocate.ie and then create new look for the main page/template every are should have its own box/ container with soft borders also logo looks too plain and can be changed if required.

```html
<!DOCTYPE html>
<html lang="en">
<head>
<meta charset="utf-8">
<title>BitLocate.ie – Car Dismantlers – Car Parts Search</title>
<link href="https://fonts.googleapis.com/css2?family=Open+Sans:ital,wght@0,400;0,600;0,700;1,400&display=swap" rel="stylesheet">
<style>
:root{
  --red:#c4161c;
  --dark-red:#8e1015;
  --blue:#0e4f9a;
  --blue-dark:#083a74;
  --text:#333;
  --muted:#6b6b6b;
  --panel:#e6e6e6;
  --panel-border:#d2d2d2;
  --white:#fff;
  --link:#1b4f9c;
}
*{box-sizing:border-box;margin:0;padding:0}
html,body{width:1200px;height:818px;overflow:hidden;background:var(--white)}
body{position:relative;font-family:"Open Sans",Verdana,sans-serif;color:var(--text)}
.user-links{position:absolute;left:907px;top:0;width:150px;height:26px;background:var(--dark-red);border-radius:0 0 6px 6px;color:var(--white);font-size:13px;display:flex;align-items:center;justify-content:center;gap:10px}
.brand{position:absolute;left:150px;top:32px;display:flex;align-items:center;gap:14px}
.brand-dot{width:56px;height:56px;border-radius:50%;background:var(--red)}
.brand-name{font-size:44px;font-weight:700;color:var(--blue);letter-spacing:-1px}
.photo{position:absolute;border-radius:6px;overflow:hidden;display:flex;align-items:flex-end;justify-content:flex-end}
.photo p{color:var(--white);font-weight:700;font-size:17px;line-height:1.25;text-align:right;padding:0 18px 14px 0}
.header-banner{left:640px;top:41px;width:428px;height:86px;background:linear-gradient(90deg,#5a0a0c,#c81d22 45%,#e44a3a 70%,#7b1014);align-items:center}
.header-banner p{padding:0 18px 0 0;font-size:18px}
.main-nav{position:absolute;left:132px;top:144px;width:936px;height:38px;background:linear-gradient(var(--blue),var(--blue-dark));border-radius:4px;display:flex;align-items:center;padding-left:18px;color:var(--white);font-size:15px;gap:9px}
.panel{position:absolute;left:132px;top:197px;width:936px;height:595px;background:linear-gradient(#f2f2f2,var(--panel));border:1px solid var(--panel-border);border-radius:10px}
.page-title{position:absolute;left:149px;top:233px;width:667px;height:38px;background:linear-gradient(#fff,#e3e3e3);border:1px solid #cfcfcf;border-radius:8px;color:var(--red);font-style:italic;font-size:21px;display:flex;align-items:center;justify-content:center}
.tab{position:absolute;top:312px;height:56px;width:175px;background:linear-gradient(#fafafa,#dedede);border:1px solid #cfcfcf;border-bottom:none;border-radius:8px 8px 0 0;color:#9a9a9a;font-style:italic;font-size:24px;display:flex;align-items:center;justify-content:center}
.tab-active{top:302px;height:66px;width:170px;background:var(--white);color:#8a8a8a;z-index:2}
.search-box{position:absolute;left:149px;top:367px;width:669px;height:346px;background:linear-gradient(var(--white),#eee);border:1px solid #cfcfcf;border-radius:0 8px 8px 8px}
.instructions{position:absolute;left:0;right:0;top:44px;text-align:center;font-size:14px;font-style:italic;color:var(--muted)}
.filters{position:absolute;left:16px;top:110px;display:flex;gap:6px}
.select{height:22px;border:1px solid #9fb2cc;background:var(--white);font-size:11px;display:flex;align-items:center;justify-content:space-between;padding-left:4px;color:#222}
.select i{width:18px;height:100%;background:linear-gradient(#d9e6f7,#a9c2e4);display:flex;align-items:center;justify-content:center}
.terms{position:absolute;left:28px;top:194px;font-size:13px}
.terms a{color:var(--link)}
.search-button{position:absolute;left:209px;top:257px;width:297px;height:48px;background:linear-gradient(#fdfdfd,#d6d6d6);border:1px solid #c3c3c3;border-radius:8px;color:#7a7a7a;font-size:18px;display:flex;align-items:center;justify-content:center}
.footer{position:absolute;left:152px;top:728px;font-size:11px;color:var(--muted);line-height:19px}
.side-one{left:838px;top:233px;width:220px;height:201px;background:radial-gradient(circle at 40% 40%,#7a7a7a,#1d1d1d 60%,#0b0b0b)}
.side-two{left:838px;top:509px;width:220px;height:201px;background:linear-gradient(135deg,#d43a2e,#9c1518 55%,#3a2a2a)}
</style>
</head>
<body>
<div class="user-links"><span>Login</span><span>|</span><span>Sign Up</span></div>
<div class="brand"><span class="brand-dot"></span><span class="brand-name">BitLocate.ie</span></div>
<div class="photo header-banner" role="img" aria-label="Close-up photograph of a red sports car wheel"><p>Lorem Ipsum is simply<br>dummy text</p></div>

<nav class="main-nav">
  <span>Parts Search</span><span>|</span><span>Parts Request</span><span>|</span><span>Damaged Repairables</span><span>|</span><span>About</span><span>|</span><span>Contact</span><span>|</span><span>Dismantlers by Map</span><span>|</span><span>Dismantlers by List</span>
</nav>

<div class="panel"></div>
<h1 class="page-title">Car Dismantlers - Car Parts Search</h1>

<div class="tab tab-active" style="left:149px">Step 1</div>
<div class="tab" style="left:329px">Step 2</div>
<div class="tab" style="left:511px">Step 3</div>

<section class="search-box">
  <p class="instructions">... Select the Make, Model &amp; Year of the vehicle for which you require parts!</p>
  <div class="filters">
    <span class="select" style="width:134px">– CAR MAKE –<i><svg width="8" height="5"><path d="M0 0h8L4 5z" fill="#2b4f86"/></svg></i></span>
    <span class="select" style="width:134px">– CAR MODEL –<i><svg width="8" height="5"><path d="M0 0h8L4 5z" fill="#2b4f86"/></svg></i></span>
    <span class="select" style="width:90px">ANY YEAR<i><svg width="8" height="5"><path d="M0 0h8L4 5z" fill="#2b4f86"/></svg></i></span>
    <span class="select" style="width:154px">– ANY CATEGORY –<i><svg width="8" height="5"><path d="M0 0h8L4 5z" fill="#2b4f86"/></svg></i></span>
    <span class="select" style="width:118px">– ANY PARTS –<i><svg width="8" height="5"><path d="M0 0h8L4 5z" fill="#2b4f86"/></svg></i></span>
  </div>
  <p class="terms">By clicking the Search button below you are agreeing with the <a href="#">Terms &amp; Conditions</a></p>
  <div class="search-button">Search Car Discmantlers</div>
</section>

<footer class="footer">
  <p>© 2009 - 2011 www.bitlocate.ie</p>
  <p>Car Dismantlers &amp; Car Breakers Search for Ireland</p>
</footer>

<div class="photo side-one" role="img" aria-label="Photograph of a dark alloy car wheel and tyre"><p>Lorem Ipsum<br>is simply<br>dummy text</p></div>
<div class="photo side-two" role="img" aria-label="Photograph of a mechanic repairing a red car engine"><p>Lorem Ipsum<br>is simply<br>dummy text</p></div>
</body>
</html>
```